" A empresa opera inteiramente o segmento de tecnologia e pesquisa, focando no desenvolvimento de soluções únicas e disruptivas, com portifólio próprio de sistemas. "

```html
<!DOCTYPE html>
<html lang="pt-BR">
<head>
<meta charset="UTF-8">
<title>NOVIRA — Cartão de visita</title>
<link rel="stylesheet" href="https://fonts.googleapis.com/css2?family=Montserrat:wght@400;500;700&display=swap">
<style>
  :root {
    --backdrop: #3b3b3b;
    --card-dark: #4a4a4a;
    --card-dark-deep: #2f2f2f;
    --card-light: #f7f7f7;
    --ink-light: #ffffff;
    --ink-dark: #3a3a3a;
    --ink-muted: #6e6e6e;
    --deco-light: #d9d9d9;
    --deco-soft: #bdbdbd;
  }
  * { margin: 0; padding: 0; box-sizing: border-box; }
  html, body { width: 1200px; height: 1200px; overflow: hidden; }
  body {
    background: var(--backdrop);
    font-family: "Montserrat", sans-serif;
    position: relative;
  }
  .card { position: absolute; border-radius: 22px; overflow: hidden; }

  /* Front card */
  .card-front {
    left: 100px; top: 150px; width: 1000px; height: 340px;
    background: linear-gradient(100deg, var(--card-dark-deep), var(--card-dark) 60%, #5a5a5a);
  }
  .card-front .decoration {
    position: absolute; left: 0; top: 0; width: 520px; height: 100%;
    background: linear-gradient(115deg, var(--deco-light) 0%, var(--deco-soft) 45%, rgba(90,90,90,0) 100%);
    opacity: 0.75;
  }
  .card-front .identity {
    position: absolute; right: 90px; top: 50%; transform: translateY(-50%);
    display: flex; flex-direction: column; align-items: flex-start; gap: 14px;
  }
  .brand { display: flex; align-items: center; gap: 16px; }
  .brand-square { width: 34px; height: 34px; background: currentColor; }
  .brand-name { font-weight: 700; letter-spacing: 3px; }
  .card-front .brand { color: var(--ink-light); }
  .card-front .brand-name { font-size: 58px; }
  .card-front .tagline {
    color: var(--ink-light); font-size: 14px; font-weight: 400;
    line-height: 1.4; max-width: 220px; opacity: 0.85;
  }

  /* Back card */
  .card-back {
    left: 290px; top: 600px; width: 620px; height: 420px;
    background: var(--card-light);
    padding: 60px 64px;
    display: flex; flex-direction: column; justify-content: space-between;
  }
  .card-back .brand { color: var(--ink-dark); }
  .card-back .brand-square { width: 28px; height: 28px; }
  .card-back .brand-name { font-size: 46px; }
  .card-back .tagline {
    color: var(--ink-muted); font-size: 14px; margin-top: 10px; max-width: 260px; line-height: 1.4;
  }
  .contacts { list-style: none; display: grid; grid-template-columns: auto auto; gap: 16px 40px; justify-content: start; }
  .contacts li {
    display: flex; align-items: center; gap: 10px;
    font-size: 18px; font-weight: 500; color: var(--ink-dark);
  }
  .contacts li.phone { grid-column: 1 / -1; }
  .contact-icon { width: 24px; height: 24px; flex-shrink: 0; }
  .social-dot { width: 22px; height: 22px; border-radius: 50%; border: 2px solid var(--ink-dark); flex-shrink: 0; }
</style>
</head>
<body>
  <section class="card card-front" aria-label="Frente do cartão">
    <div class="decoration" role="img" aria-label="Grande forma gráfica da marca em faixas diagonais claras"></div>
    <div class="identity">
      <div class="brand">
        <span class="brand-square"></span>
        <span class="brand-name">NOVIRA</span>
      </div>
      <p class="tagline">tecnologia e pesquisa em soluções próprias</p>
    </div>
  </section>

  <section class="card card-back" aria-label="Verso do cartão">
    <header>
      <div class="brand">
        <span class="brand-square"></span>
        <span class="brand-name">NOVIRA</span>
      </div>
      <p class="tagline">tecnologia e pesquisa em soluções próprias</p>
    </header>
    <ul class="contacts">
      <li class="phone">
        <svg class="contact-icon" viewBox="0 0 24 24" fill="none" stroke="#3a3a3a" stroke-width="1.8" stroke-linejoin="round">
          <path d="M5 3h4l2 5-2.5 1.5a11 11 0 0 0 6 6L16 13l5 2v4a2 2 0 0 1-2 2A17 17 0 0 1 3 5a2 2 0 0 1 2-2z"/>
        </svg>
        21 90412-3376
      </li>
      <li class="social">
        <span class="social-dot"></span>
        @novira
      </li>
      <li class="web">
        <svg class="contact-icon" viewBox="0 0 24 24" fill="none" stroke="#3a3a3a" stroke-width="1.8">
          <circle cx="12" cy="12" r="9"/>
          <ellipse cx="12" cy="12" rx="4" ry="9"/>
          <line x1="3" y1="12" x2="21" y2="12"/>
        </svg>
        novira.com
      </li>
    </ul>
  </section>
</body>
</html>
```